Flyer-Design für den Bereich Familienfotografie
Helene hat hervorragende Arbeit geleistet. Der erste Wurf war schon überzeugend. Änderungswünsche zum finalen Design wurden schnell und gut umgesetzt und besonders gefallen haben mir die von ihr proaktiv eingebrachten Ideen und Lösungsvorschläge. Vielen Dank!
Zielgruppe
Ich bin ein Fotograf mit dem Schwerpunkt Familienfotos und Reportagen
Aufgabenstellung
Hier soll ein Flyer für den Bereich Familienfotografie entstehen. Also Schwangerschaft, Baby, Familien, Portrait & Pärchen. Er soll Infos zu meinem Leistungsumfang und zum Ablauf von Buchungen, Shootings und Bildauswahl transtportieren. Hier gerne erstmal Blindtext vorsehen, ich liefere dann Inhalt nach.
Infos und weitere Eindrücke gibts auf www.bernhardlossow.de
Die beigefügten Bilder müssen natürlich nicht alle genutzt werden, vor Erstellung der Druckdaten suche ich die Bilder auch noch ohne Logo und in einer höheren Auflösung heraus, zur Gestaltung sollte das aber reichen.
Als Format wäre Din lang hochkant mit 6-8 Seiten ganz schön, (wegen Postversand im Brief/Rechnungsumschlag). Wenn Ihr gute Gründe für anderes liefert, lassen ich mich aber sicher auch überzeugen.
Optisch soll der Flyer schon auffallen, also etwas mehr als ein paar Fotos und Text drauffallen lassen, bitte aber kein verschnörkelter pastell 'Schi-Schi' wie er immer mal wieder aus dem anglophonen Raum zu uns schwappt ;)
Ich freue mich auf Eure Ideen!
Im Nachgang zu diesem Projekt sollen dann auf der Basis noch Flyer für Hochzeiten und Reportagen erstellt werden, sowie in 2019 auch neue Visitenkarten und ein Portfolio-Booklet. Diese Aufträge gehen dann natürlich auch an den oder diejenige, die sich bei dem 'Familienflyer' durchsetzt.
Falls Fragen oder Unklarheiten aufkommen, lasst es mich gerne wissen! Kontaktdaten findet Ihr auf meiner Seite.
Generell habe ich mich vielleicht noch nicht klar genug ausgedrückt (sorry, ist mein erstes Projekt hier)
Der Flyer soll natürlich die Wertigkeit und Professionalität meiner Arbeit widerspiegeln. Ganz klar soll er NICHT so aussehen, als hätte man das Ganze in 3 min in Powerpoint zusammengeklickt.
Es muss direkt klar werden, dass es in dem Flyer um die Familienfotografie geht und es sollen alle 4 Bereiche (Schwangerschaft, Baby, Familien, Portraits/Pärchen) darges..

```html
<!DOCTYPE html>
<html lang="de">
<head>
<meta charset="utf-8">
<title>Familienfotografie – Flyer</title>
<link href="https://fonts.googleapis.com/css2?family=Arimo&family=Montserrat:wght@400;700&family=PT+Serif&display=swap" rel="stylesheet">
<style>
  :root {
    --paper: #ffffff;
    --accent: #f2445a;
    --ink: #3d3d3d;
    --ink-soft: #2b2b2b;
    --rule-dark: #444444;
    --on-accent: #ffffff;
  }
  html, body { margin: 0; padding: 0; overflow: hidden; background: var(--paper); }
  .flyer {
    position: relative;
    width: 1200px;
    height: 927px;
    overflow: hidden;
    background: var(--paper);
    font-family: "Montserrat", sans-serif;
    color: var(--ink-soft);
  }
  .photo { position: absolute; }

  /* Left panel */
  .portrait { left: 122px; top: 12px; width: 172px; height: 258px;
    background: linear-gradient(160deg, #3a3a3e 0%, #1c1c20 60%, #2a2f3a 100%); }
  .section-title {
    position: absolute; margin: 0;
    font-family: "PT Serif", serif; font-weight: 400;
    font-size: 43px; line-height: 1; color: var(--ink);
  }
  .mission-title { left: 41px; top: 301px; }
  .rule { position: absolute; height: 4px; }
  .mission-rule { left: 41px; top: 381px; width: 328px; background: var(--accent); }
  .mission-text {
    position: absolute; left: 41px; top: 424px; width: 336px; margin: 0;
    font-size: 13.6px; line-height: 20.6px; letter-spacing: 0.3px; color: var(--ink-soft);
  }
  .mission-text p { margin: 0 0 20.6px; }
  .mission-text .sign { margin-top: 41px; }

  /* Middle panel */
  .accent-panel { position: absolute; left: 402px; top: 0; width: 403px; height: 927px; background: var(--accent); }
  .couple   { left: 417px; top: 13px;  width: 181px; height: 257px; background: linear-gradient(180deg, #d9ecf8 0%, #f4f1dc 45%, #7fa24a 100%); }
  .father   { left: 610px; top: 13px;  width: 182px; height: 257px; background: linear-gradient(160deg, #1a1a1a 0%, #6a5a58 55%, #c9a9a7 100%); }
  .baby     { left: 417px; top: 662px; width: 181px; height: 256px; background: linear-gradient(170deg, #8fb85a 0%, #a6c47a 45%, #8a7f6e 100%); }
  .girl     { left: 610px; top: 662px; width: 182px; height: 256px; background: linear-gradient(170deg, #141414 0%, #7a5a3a 45%, #c3b2b6 100%); }
  .claim {
    position: absolute; left: 448px; top: 370px; margin: 0;
    font-family: "Arimo", sans-serif; font-size: 34px; line-height: 1;
    color: var(--on-accent);
  }
  .claim span { display: block; height: 84px; }

  /* Right panel */
  .services-title { left: 840px; top: 34px; }
  .services-rule { left: 841px; top: 111px; width: 327px; background: var(--rule-dark); }
  .service { position: absolute; left: 841px; width: 330px; }
  .service h3 {
    margin: 0; font-size: 17px; line-height: 27px; font-weight: 700;
    letter-spacing: 1.2px; color: var(--accent);
  }
  .service p {
    margin: 12px 0 0; font-size: 13.4px; line-height: 20.6px;
    letter-spacing: 0.9px; color: var(--ink-soft); word-break: break-all;
  }
  .service-family { top: 150px; }
  .service-wedding { top: 320px; }
  .service-report { top: 482px; }
</style>
</head>
<body>
<div class="flyer">
  <section class="panel-mission">
    <div class="photo portrait" role="img" aria-label="Porträt des Fotografen mit Kamera"></div>
    <h2 class="section-title mission-title">Meine Mission</h2>
    <div class="rule mission-rule"></div>
    <div class="mission-text">
      <p>Ob nun im Studio oder draußen in der Natur in Buxtehude, dem Alten Land und Umgebung, jedes Shooting ist einzigartig und es braucht Kreativität, Spontanität, Einfühlungsvermögen und ein waches Auge. Genau das mag ich an meiner Arbeit, wenn ich dann den Auslöser drücke, und mir das vertraute Klacken der Kamera sagt:</p>
      <p>„ … Bild im Kasten“</p>
      <p class="sign">Ihr<br>Bernhard Lossow</p>
    </div>
  </section>

  <section class="accent-panel"></section>
  <div class="photo couple" role="img" aria-label="Paar küsst sich auf einer sonnigen Wiese"></div>
  <div class="photo father" role="img" aria-label="Vater umarmt lachende Tochter"></div>
  <p class="claim"><span>Momente.</span><span>Festgehalten.</span><span>Für immer.</span></p>
  <div class="photo baby" role="img" aria-label="Baby krabbelt auf einem Baumstamm im Grünen"></div>
  <div class="photo girl" role="img" aria-label="Mädchen beugt sich lachend nach vorn"></div>

  <section class="panel-services">
    <h2 class="section-title services-title">Leistungen</h2>
    <div class="rule services-rule"></div>
    <div class="service service-family">
      <h3>FAMILIE.SCHWANGERSCHAFT.<br>BABYS.</h3>
      <p>blindextblindextblindextblindextblindextblindextblindextblindextblindextblindextblindextblindext</p>
    </div>
    <div class="service service-wedding">
      <h3>HOCHZEIT. PORTRAIT.</h3>
      <p>blindextblindextblindextblindextblindextblindextblindextblindextblindextblindextblindextblindextblindextblindextblindextblindext</p>
    </div>
    <div class="service service-report">
      <h3>REPORTAGE.</h3>
      <p>blindextblindextblindextblindextblindextblindextblindextblindextblindextblindextblindextblindextblindextblindext</p>
    </div>
  </section>
</div>
</body>
</html>
```